Flyer for a Business Consultant

I need a one-page description of services. I am a Brennick Certifed Talents Mentor. I do not have a personal website but think I will soon purchase this template https://varlowskins.example/skins/lectern/. I like the larger font, simplicity and larger font. I will attach his pricing flyer which I like - not to overly guide or restrict your creative thinking, but only to give a little perspective. I don't like busy, noisy - I like clarity, simplicity. Here 's the Brennick website which these same traits https://www.brennicktalentshub.example/ and can be a source of ideas and colors.

Target Market(s)

CEOs and Middle Managers in organizations

Industry/Entity Type

Financial Service

Colors

Designer to choose colors to be used in the design.

Requirements
Must have
• Clarity, simplicity, but also strength (not weak or frilly looking)
Nice to have
• Warm color(s), larger/not skinny font
Should not have
• Loud, noisy, busy

```html
<!DOCTYPE html>
<html lang="en">
<head>
<meta charset="utf-8">
<title>A Strength-Based Approach to Managing Team Effectiveness</title>
<link rel="stylesheet" href="https://fonts.googleapis.com/css2?family=Source+Sans+3:ital,wght@0,400;0,600;0,700;1,400&display=swap">
<style>
  :root {
    --stage: #5a5c5e;
    --paper: #ffffff;
    --ink: #1e1e1e;
    --brand-blue: #1a8fd8;
    --pill-top: #35b3f0;
    --pill-bottom: #0f84cf;
    --panel-1: #1b82d2;
    --panel-2: #1c6fc4;
    --panel-3: #1f3f9c;
    --band: rgba(12, 22, 64, 0.85);
    --muted: #555;
    --rule: #9a9a9a;
  }
  * { box-sizing: border-box; margin: 0; padding: 0; }
  html, body { width: 975px; height: 1200px; overflow: hidden; }
  body {
    background: var(--stage);
    font-family: "Source Sans 3", Arial, sans-serif;
    color: var(--ink);
    position: relative;
  }
  .flyer {
    position: absolute; left: 83px; top: 76px;
    width: 809px; height: 1047px;
    background: var(--paper);
  }
  .headline { position: absolute; top: 36px; left: 0; width: 100%; text-align: center; }
  .headline__kicker { font-size: 34px; font-weight: 400; letter-spacing: 0.2px; line-height: 38px; color: #222; }
  .headline__main { font-size: 45px; font-weight: 700; color: var(--brand-blue); line-height: 48px; letter-spacing: 0.3px; }
  .hero {
    position: absolute; top: 132px; left: 0; width: 809px; height: 345px;
    background: radial-gradient(ellipse at 50% 45%, #c9a48c 0%, #8f7f78 30%, #3c4356 65%, #d9dde2 100%);
  }
  .hero__band {
    position: absolute; left: 0; bottom: 0; width: 100%; height: 36px;
    background: linear-gradient(90deg, rgba(12,22,64,0) 0%, var(--band) 25%, var(--band) 75%, rgba(12,22,64,0) 100%);
    color: #fff; font-weight: 700; font-size: 19px; text-align: center; line-height: 36px; letter-spacing: 0.3px;
  }
  .benefits { position: absolute; top: 477px; left: 0; width: 809px; height: 157px; display: flex; }
  .benefit {
    flex: 1; color: #fff; text-align: center;
    font-weight: 700; font-size: 13.5px; line-height: 17px; text-transform: uppercase;
    padding-top: 12px;
  }
  .benefit:nth-child(1) { background: var(--panel-1); }
  .benefit:nth-child(2) { background: var(--panel-2); }
  .benefit:nth-child(3) { background: var(--panel-3); }
  .benefit svg { display: block; margin: 0 auto 14px; }
  .services { position: absolute; top: 657px; left: 59px; width: 694px; }
  .service__label {
    display: block; width: 260px; height: 28px; margin: 0 auto 11px;
    border-radius: 14px;
    background: linear-gradient(var(--pill-top), var(--pill-bottom));
    color: #fff; font-weight: 700; font-size: 13px; text-align: center; line-height: 28px; letter-spacing: 0.3px;
  }
  .service__text { font-size: 13px; font-weight: 600; line-height: 16.5px; margin-bottom: 8px; }
  .service + .service .service__label { margin-top: 0; }
  .service:nth-child(3) .service__label { margin-top: 10px; }
  .footer { position: absolute; top: 964px; left: 47px; width: 720px; height: 62px; }
  .credential {
    position: absolute; left: 0; top: 0; width: 221px; height: 62px;
    border: 1px solid #b9b9b9; display: flex; align-items: center; padding-left: 17px; gap: 9px;
  }
  .credential__mark { width: 40px; height: 40px; background: #8a8a8a; flex: none; }
  .credential__name { font-size: 14px; line-height: 16px; color: #666; font-weight: 400; }
  .coach { position: absolute; left: 244px; top: 10px; width: 200px; text-align: center; }
  .coach__name { font-size: 23px; font-weight: 700; color: var(--brand-blue); line-height: 26px; }
  .coach__title { font-size: 11px; font-style: italic; color: #333; }
  .divider { position: absolute; left: 474px; top: 8px; width: 1px; height: 50px; background: var(--rule); }
  .contact { position: absolute; left: 494px; top: 8px; }
  .contact__row { display: flex; align-items: center; gap: 10px; }
  .contact__phone { font-size: 24px; color: #222; line-height: 30px; }
  .contact__email { font-size: 13.5px; font-weight: 700; color: #222; }
</style>
</head>
<body>
  <main class="flyer">
    <header class="headline">
      <h2 class="headline__kicker">A STRENGTH-BASED APPROACH TO</h2>
      <h1 class="headline__main">MANAGING TEAM EFFECTIVENESS</h1>
    </header>

    <section class="hero" role="img" aria-label="Photo of a smiling business team joining hands in a high-five huddle">
      <div class="hero__band">WE HELP TEAMS GROW STRONGER BY</div>
    </section>

    <section class="benefits">
      <div class="benefit">
        <svg width="64" height="64" viewBox="0 0 64 64" aria-hidden="true">
          <rect x="14" y="6" width="14" height="34" rx="6" fill="#fff" transform="rotate(-30 21 23)"/>
          <rect x="36" y="6" width="14" height="34" rx="6" fill="#fff" transform="rotate(30 43 23)"/>
          <rect x="6" y="42" width="20" height="14" rx="3" fill="#fff"/>
          <rect x="38" y="42" width="20" height="14" rx="3" fill="#fff"/>
          <rect x="20" y="28" width="24" height="16" rx="7" fill="#fff"/>
        </svg>
        Bringing a deep awareness<br>of their strengths and<br>the strengths of their<br>associates.
      </div>
      <div class="benefit">
        <svg width="64" height="64" viewBox="0 0 64 64" aria-hidden="true">
          <rect x="19" y="2" width="26" height="16" rx="8" fill="#fff"/>
          <path d="M26 17 L24 24 L32 17 Z" fill="#fff"/>
          <circle cx="26" cy="10" r="2" fill="var(--panel-2)"/><circle cx="32" cy="10" r="2" fill="var(--panel-2)"/><circle cx="38" cy="10" r="2" fill="var(--panel-2)"/>
          <circle cx="17" cy="33" r="7" fill="#fff"/><path d="M5 62 V52 Q5 42 17 42 Q29 42 29 52 V62 Z" fill="#fff"/>
          <circle cx="47" cy="33" r="7" fill="#fff"/><path d="M35 62 V52 Q35 42 47 42 Q59 42 59 52 V62 Z" fill="#fff"/>
        </svg>
        Increasing the team’s<br>communication and sense<br>of partnership.
      </div>
      <div class="benefit">
        <svg width="64" height="64" viewBox="0 0 64 64" aria-hidden="true">
          <circle cx="12" cy="12" r="6" fill="#fff"/><rect x="5" y="20" width="14" height="28" rx="4" fill="#fff"/>
          <circle cx="32" cy="10" r="7" fill="#fff"/><rect x="24" y="19" width="16" height="34" rx="4" fill="#fff"/>
          <circle cx="52" cy="12" r="6" fill="#fff"/><rect x="45" y="20" width="14" height="28" rx="4" fill="#fff"/>
        </svg>
        Improving employee<br>engagement and<br>effectiveness.
      </div>
    </section>

    <section class="services">
      <article class="service">
        <h3 class="service__label">INDIVIDUAL SESSIONS</h3>
        <p class="service__text">Conversational feedback and coaching sessions based on Brennick’s TalentPrint assessments. These sessions last about an hour and lead to a personalized translation of the results and how their strengths show up in their work and inherent blind spots they bring.</p>
      </article>
      <article class="service">
        <h3 class="service__label">STRENGTH DISCOVERY WORKSHOP</h3>
        <p class="service__text">A retreat-style Team Workshop in which the team learns each other’s unique Top 5 strengths. The session is very interactive and provides a common language that leads to improved communication and effectiveness. Tailored in 2.3.and 4-hour options are tailored to your Team’s challenges and opportunities.</p>
      </article>
      <article class="service">
        <h3 class="service__label">FOLLOW-ON MODULES</h3>
        <p class="service__text">Follow-on is important to make the insights learned to be practical and integrated into the Teams’ approach and workflows. In a debrief session included as part of the workshop, we provide several 15-minute exercise modules for use in regular meetings, and we offer guest facilitated modules of 30- 60 minutes each.</p>
      </article>
    </section>

    <footer class="footer">
      <div class="credential">
        <span class="credential__mark"></span>
        <span class="credential__name">Brennick Certifed<br>Talents Mentor</span>
      </div>
      <div class="coach">
        <div class="coach__name">Marcus Delaney</div>
        <div class="coach__title">Brennick Workplace Talents Mentor</div>
      </div>
      <div class="divider"></div>
      <div class="contact">
        <div class="contact__row">
          <svg width="14" height="14" viewBox="0 0 24 24" aria-hidden="true"><path fill="var(--brand-blue)" d="M6.6 10.8a15 15 0 0 0 6.6 6.6l2.2-2.2a1 1 0 0 1 1-.25 11.4 11.4 0 0 0 3.6.57 1 1 0 0 1 1 1V20a1 1 0 0 1-1 1A17 17 0 0 1 3 4a1 1 0 0 1 1-1h3.5a1 1 0 0 1 1 1c0 1.25.2 2.45.57 3.6a1 1 0 0 1-.25 1z"/></svg>
          <span class="contact__phone">555-014-2738</span>
        </div>
        <div class="contact__row">
          <svg width="14" height="12" viewBox="0 0 24 20" aria-hidden="true"><rect x="1" y="2" width="22" height="16" rx="2" fill="var(--brand-blue)"/><path d="M2 3 L12 11 L22 3" stroke="#fff" stroke-width="2" fill="none"/></svg>
          <span class="contact__email">marcus@talentsiq.example</span>
        </div>
      </div>
    </footer>
  </main>
</body>
</html>
```